WBL Kids Choir

Card to hand out or mail out with our own mailing labels. Needs to be appealing to families with children ages 4 yrs through 6th grade, who have an interest in musical experiences for the kids in a contemporary Bible teaching/church setting. We have 3 different kids choirs: 4-yr-old & Kindergarten Choir, 1st-3rd grade choir, and 4th-6th grade choir. This is a FREE after-school program every Tuesday from 3:30-5:00. Transportation for grades 1-6 from local schools is provided. Parents should expect their children to experience fun, friends, music, recreation, games, snacks, character building, Bible teaching, in an encouraging church environment.

Industry/Entity Type

Church

Requirements
Nice to have
• Bight colors

```html
<!DOCTYPE html>
<html lang="en">
<head>
<meta charset="utf-8">
<title>WBL Kids Choir</title>
<link rel="stylesheet" href="https://fonts.googleapis.com/css2?family=Fira+Sans+Condensed:ital,wght@0,400;0,600;0,700;1,700&display=swap">
<style>
  :root {
    --red: #9b1c20;
    --blue: #253f8e;
    --yellow: #f4e517;
    --ink: #111111;
    --white: #ffffff;
    --paper: #ffffff;
  }
  html, body {
    margin: 0;
    padding: 0;
    overflow: hidden;
    background: var(--paper);
  }
  .card {
    position: relative;
    width: 1200px;
    height: 930px;
    background: var(--paper);
    font-family: "Fira Sans Condensed", "Arial Narrow", sans-serif;
    color: var(--ink);
    overflow: hidden;
  }
  .kids-photo {
    position: absolute;
    left: 29px;
    top: 29px;
    width: 302px;
    height: 202px;
    background:
      radial-gradient(circle at 50% 55%, #f3c9a8 0 28%, transparent 29%),
      linear-gradient(135deg, #3aa7e0 0%, #7cc5ee 30%, #e94a3b 55%, #f6c623 78%, #4fb548 100%);
  }
  .headline {
    position: absolute;
    left: 369px;
    top: 44px;
    width: 800px;
    margin: 0;
    font-weight: 700;
    font-size: 45px;
    line-height: 44px;
    letter-spacing: -0.3px;
  }
  .choir-band {
    position: absolute;
    left: 334px;
    width: 866px;
    height: 133px;
    box-sizing: border-box;
    padding: 8px 0 0 35px;
  }
  .choir-band h2 {
    margin: 0 0 4px;
    font-weight: 700;
    font-size: 35px;
    line-height: 44px;
  }
  .choir-band p {
    margin: 0;
    font-size: 21px;
    line-height: 26px;
    width: 790px;
  }
  .choir-band--little { top: 271px; background: var(--red); color: var(--white); }
  .choir-band--middle { top: 423px; background: var(--blue); color: var(--white); }
  .choir-band--older  { top: 577px; background: var(--yellow); color: var(--ink); }

  .ministry-name {
    position: absolute;
    left: 43px;
    top: 330px;
    width: 257px;
    text-align: center;
    color: var(--red);
    font-weight: 600;
    font-size: 26px;
    line-height: 32px;
  }
  .ministry-name small {
    display: block;
    font-size: 17px;
    line-height: 22px;
    margin-top: 10px;
  }
  .church-name {
    position: absolute;
    left: 50px;
    top: 680px;
    width: 236px;
    text-align: center;
    color: var(--blue);
    font-weight: 700;
    font-size: 34px;
    line-height: 40px;
    letter-spacing: 2px;
    text-transform: uppercase;
  }
  .schedule {
    position: absolute;
    left: 369px;
    top: 762px;
    margin: 0;
    font-size: 29px;
    line-height: 40px;
  }
  .schedule strong { font-weight: 700; }
  .transport {
    position: absolute;
    left: 379px;
    top: 838px;
    display: flex;
    align-items: center;
    gap: 16px;
    margin: 0;
    color: var(--red);
    font-weight: 700;
    font-style: italic;
    font-size: 23px;
  }
  .transport svg { flex: none; }
</style>
</head>
<body>
  <main class="card">
    <div class="kids-photo" role="img" aria-label="Photo of smiling children in colourful shirts huddled in a circle against a blue sky"></div>

    <h1 class="headline">Do you have an interest in musical experiences for your kids in a contemporary Bible teaching and church setting?</h1>

    <div class="ministry-name">Children’s Ministry<small>Grace Valley Church<br>Pine Hollow, Kansas</small></div>

    <section class="choir-band choir-band--little">
      <h2>4-yr-old &amp; Kindergarten Choir</h2>
      <p>Sed ut perspiciatis unde omnis iste natus error sit voluptatem accusantium doloremque laudantium, totam rem aperiam, eaque ipsa quae ab illo inventore.</p>
    </section>

    <section class="choir-band choir-band--middle">
      <h2>1st-3rd grade choir</h2>
      <p>Sed ut perspiciatis unde omnis iste natus error sit voluptatem accusantium doloremque laudantium, totam rem aperiam, eaque ipsa quae ab illo inventore.</p>
    </section>

    <section class="choir-band choir-band--older">
      <h2>4th-6th grade choir</h2>
      <p>Sed ut perspiciatis unde omnis iste natus error sit voluptatem accusantium doloremque laudantium, totam rem aperiam, eaque ipsa quae ab illo inventore.</p>
    </section>

    <div class="church-name">Grace Valley Church</div>

    <p class="schedule"><strong>FREE</strong> after-school program every <strong>Tuesday</strong> from <strong>3:30-5:00.</strong></p>

    <p class="transport">
      <svg width="36" height="26" viewBox="0 0 36 26" aria-hidden="true">
        <path d="M7 4 Q8 1 11 1 H25 Q28 1 29 4 L31 10 H33 Q35 10 35 12 V19 Q35 21 33 21 H3 Q1 21 1 19 V12 Q1 10 3 10 H5 Z" fill="#9b1c20"/>
        <path d="M9 5 H27 L28.5 10 H7.5 Z" fill="#ffffff"/>
        <circle cx="8" cy="15" r="2" fill="#ffffff"/>
        <circle cx="28" cy="15" r="2" fill="#ffffff"/>
        <rect x="3" y="20" width="6" height="5" rx="1.5" fill="#9b1c20"/>
        <rect x="27" y="20" width="6" height="5" rx="1.5" fill="#9b1c20"/>
      </svg>
      Transportation for grades 1-6 from local schools is provided.
    </p>
  </main>
</body>
</html>
```